Business Card For Kelmora Financial Consulting

Hi, I would like a business card designed. Bold, modern.
Please use the same design as the logo. I have also attached the website design to see the overall theme.
Wordmark Font
Color: Hex: #01AEF7

```html
<!DOCTYPE html>
<html lang="en">
<head>
<meta charset="utf-8">
<title>Kelmora Financial Consulting – Business Card</title>
<link href="https://fonts.googleapis.com/css2?family=Open+Sans:wght@400;700&display=swap" rel="stylesheet">
<style>
  :root {
    --backdrop: #222222;
    --card-navy: #0a4468;
    --card-edge: #3aa6dd;
    --accent-blue: #35a9e1;
    --text-white: #ffffff;
  }
  * { margin: 0; padding: 0; box-sizing: border-box; }
  html, body { width: 1200px; height: 780px; overflow: hidden; background: var(--backdrop); }
  body { font-family: "Open Sans", Arial, sans-serif; position: relative; }

  .card {
    position: absolute;
    top: 240px;
    width: 520px;
    height: 300px;
    background: var(--card-navy);
    border-top: 2px solid var(--card-edge);
    border-left: 2px solid var(--card-edge);
    box-shadow: 0 18px 40px rgba(0,0,0,.55);
  }
  .card--back { left: 50px; }
  .card--front { left: 630px; display: flex; align-items: center; justify-content: center; }

  .brand { display: flex; align-items: center; gap: 12px; }
  .brand__mark { width: 14px; height: 14px; background: var(--accent-blue); flex: none; }
  .brand__name {
    color: var(--text-white);
    font-weight: 700;
    font-size: 26px;
    letter-spacing: .04em;
    text-transform: uppercase;
    line-height: 1.2;
  }
  .card--back .brand { position: absolute; left: 34px; top: 30px; gap: 8px; }
  .card--back .brand__mark { width: 9px; height: 9px; }
  .card--back .brand__name { font-size: 15px; }

  .contact { position: absolute; left: 34px; bottom: 32px; color: var(--text-white); font-size: 12.5px; line-height: 1.55; }
  .contact__address { margin-bottom: 6px; }
  .contact__row { display: flex; align-items: center; gap: 8px; }
  .contact__icon { width: 12px; height: 12px; flex: none; }

  .person { position: absolute; right: 34px; bottom: 40px; text-align: right; }
  .person__name { color: var(--accent-blue); font-weight: 700; font-size: 22px; line-height: 1.2; }
  .person__title { color: var(--text-white); font-size: 13px; }
  .person__tab { position: absolute; right: 0; bottom: 30px; width: 12px; height: 34px; background: var(--accent-blue); }
</style>
</head>
<body>

<section class="card card--back" aria-label="Business card, contact side">
  <div class="brand">
    <span class="brand__mark"></span>
    <span class="brand__name">Kelmora Financial Consulting</span>
  </div>

  <div class="contact">
    <p class="contact__address">480 Harlow Ave. Suite 310<br>Denton, TX 76201</p>
    <p class="contact__row">
      <svg class="contact__icon" viewBox="0 0 24 24" aria-hidden="true"><path fill="#35a9e1" d="M6.6 10.8a15 15 0 0 0 6.6 6.6l2.2-2.2a1 1 0 0 1 1-.25 11.4 11.4 0 0 0 3.6.57 1 1 0 0 1 1 1V20a1 1 0 0 1-1 1A17 17 0 0 1 3 4a1 1 0 0 1 1-1h3.5a1 1 0 0 1 1 1c0 1.25.2 2.45.57 3.6a1 1 0 0 1-.25 1z"/></svg>
      (555) 014-2290
    </p>
    <p class="contact__row">
      <svg class="contact__icon" viewBox="0 0 24 24" aria-hidden="true"><rect x="2" y="5" width="20" height="14" rx="2" fill="#35a9e1"/><path d="M3 6l9 7 9-7" fill="none" stroke="#0a4468" stroke-width="2"/></svg>
      info@kelmora.com
    </p>
    <p class="contact__row">
      <svg class="contact__icon" viewBox="0 0 24 24" aria-hidden="true"><circle cx="12" cy="12" r="10" fill="#35a9e1"/><path d="M2 12h20M12 2c3 3 3 17 0 20M12 2c-3 3-3 17 0 20" fill="none" stroke="#0a4468" stroke-width="1.6"/></svg>
      www.kelmora.com
    </p>
  </div>

  <div class="person">
    <p class="person__name">Lena Varossi</p>
    <p class="person__title">Managing Director</p>
  </div>
  <span class="person__tab"></span>
</section>

<section class="card card--front" aria-label="Business card, brand side">
  <div class="brand">
    <span class="brand__mark"></span>
    <span class="brand__name">Kelmora Financial Consulting</span>
  </div>
</section>

</body>
</html>
```